KVT Calculator

We have a calculator already created however the design seems to be very boring and bland. The calculators goal is to show graphic designers, web development firms, pr agencies, marketing firms how much revenue they can potentially make by offering a managed social media solution to their clients.

We want a great designer to make the calculator appealing to our audience.

It is an amazing offer and opportunity however I do not believe the current design does it justice

you can view and play with calculator live at http://sandbox.plorvinix.com/qzta/

```html
<!DOCTYPE html>
<html lang="en">
<head>
<meta charset="utf-8">
<title>Social Media Revenue Calculator</title>
<link rel="stylesheet" href="https://fonts.googleapis.com/css2?family=Open+Sans:wght@400;600;700&display=swap">
<style>
:root{
  --wood-light:#a0643a;
  --wood-dark:#6e3f20;
  --panel:#b4bac6;
  --table:#2f2f2f;
  --row-line:#4a4a4a;
  --card:#ffffff;
  --cell:#f7f7f7;
  --cell-line:#d5d5d5;
  --ink:#3d3d3d;
  --blue-top:#3c58ab;
  --blue-bottom:#1e347e;
  --orange-top:#ff9a00;
  --orange-bottom:#ff5500;
  --track:#1b2f6e;
  --label:#ffffff;
}
*{box-sizing:border-box;margin:0;padding:0}
html,body{width:1200px;height:599px;overflow:hidden}
body{position:relative;font-family:"Open Sans",Arial,sans-serif;color:var(--ink)}
.backdrop{position:absolute;inset:0;background:linear-gradient(90deg,var(--wood-dark),var(--wood-light) 30%,#8a5230 55%,var(--wood-light) 80%,var(--wood-dark))}
.panel{position:absolute;left:51px;top:37px;width:1096px;height:516px;background:var(--panel)}
.table-bg{position:absolute;left:113px;top:75px;width:977px;height:330px;background:var(--table);box-shadow:0 8px 14px rgba(0,0,0,.35)}
.term-card{position:absolute;left:124px;top:57px;width:165px;height:463px;background:var(--card);box-shadow:0 2px 6px rgba(0,0,0,.3)}
.term-title{position:absolute;left:7px;top:7px;width:152px;height:43px;background:linear-gradient(#3a3a3a,#141414);border-radius:3px;color:#fff;font-weight:600;font-size:18px;line-height:43px;text-align:center}
.term-slider{position:absolute;left:0;top:0}
.row-label{position:absolute;left:298px;color:var(--label);font-weight:700;font-size:21px;line-height:25px}
.row-line{position:absolute;left:292px;width:225px;height:1px;background:var(--row-line)}
.plan{position:absolute;top:57px;width:176px;height:355px;background:var(--card);box-shadow:0 2px 6px rgba(0,0,0,.35)}
.plan-head{position:absolute;left:4px;top:3px;width:168px;height:61px;border-radius:4px;color:#fff;font-size:21px;font-weight:600;line-height:58px;text-align:center;background:linear-gradient(var(--blue-top),var(--blue-bottom))}
.plan--pro .plan-head{background:linear-gradient(var(--orange-top),var(--orange-bottom))}
.plan-cell{position:absolute;left:0;width:176px;height:70px;background:var(--cell);border-top:1px solid var(--cell-line);font-size:21px;line-height:70px;text-align:center}
.plan-cell--profit{font-weight:700;font-size:19px;height:62px;line-height:78px}
.step{position:absolute;top:22px;width:26px;height:26px;border-radius:50%;background:linear-gradient(#f4f4f4,#cfcfcf);border:1px solid #bdbdbd}
.step--minus{left:6px}.step--plus{right:6px}
.step::before,.step::after{content:"";position:absolute;left:7px;top:11px;width:10px;height:3px;background:#333}
.step--minus::after{display:none}
.step--plus::after{transform:rotate(90deg)}
.plan-bar{position:absolute;left:4px;bottom:5px;width:168px;height:16px;border-radius:2px;background:linear-gradient(var(--blue-top),var(--blue-bottom))}
.plan--pro .plan-bar{background:linear-gradient(var(--orange-top),var(--orange-bottom))}
.total{position:absolute;left:307px;top:441px;width:782px;height:79px;background:linear-gradient(#ffffff,#e6e6e6);box-shadow:0 2px 5px rgba(0,0,0,.3);font-size:33px;line-height:81px;text-align:center;color:#333}
.total strong{font-weight:700}
</style>
</head>
<body>
<div class="backdrop" role="img" aria-label="Wood grain tabletop backdrop"></div>
<div class="panel"></div>
<div class="table-bg"></div>

<div class="term-card">
  <div class="term-title">TERM (YRS)</div>
  <svg class="term-slider" width="165" height="463" viewBox="0 0 165 463">
    <g stroke="#d9d9d9" stroke-width="1">
      <line x1="56" y1="115" x2="102" y2="115"/><line x1="56" y1="149" x2="102" y2="149"/>
      <line x1="56" y1="183" x2="102" y2="183"/><line x1="56" y1="218" x2="102" y2="218"/>
      <line x1="56" y1="252" x2="102" y2="252"/><line x1="56" y1="286" x2="102" y2="286"/>
      <line x1="56" y1="321" x2="102" y2="321"/><line x1="56" y1="355" x2="102" y2="355"/>
      <line x1="56" y1="389" x2="102" y2="389"/>
    </g>
    <rect x="69" y="98" width="17" height="313" rx="8.5" fill="var(--track)"/>
    <rect x="71" y="149" width="13" height="260" rx="6.5" fill="#3550a6"/>
    <circle cx="77" cy="149" r="19" fill="#fafafa" stroke="#cfcfcf"/>
    <circle cx="77" cy="149" r="9" fill="#9a9a9a" stroke="#777"/>
  </svg>
</div>

<div class="row-label" style="top:141px">Clients per month:</div>
<div class="row-line" style="top:187px"></div>
<div class="row-label" style="top:211px">Your cost:</div>
<div class="row-line" style="top:257px"></div>
<div class="row-label" style="top:281px">Client pays:</div>
<div class="row-line" style="top:328px"></div>
<div class="row-label" style="top:343px">Monthly profit:<br>(year 8)</div>

<div class="plan plan--basic" style="left:517px">
  <div class="plan-head">BASIC</div>
  <div class="plan-cell" style="top:60px">1<span class="step step--minus"></span><span class="step step--plus"></span></div>
  <div class="plan-cell" style="top:130px">$197</div>
  <div class="plan-cell" style="top:201px">$297<span class="step step--minus"></span><span class="step step--plus"></span></div>
  <div class="plan-cell plan-cell--profit" style="top:271px">$9,600</div>
  <div class="plan-bar"></div>
</div>

<div class="plan plan--pro" style="left:709px">
  <div class="plan-head">PRO</div>
  <div class="plan-cell" style="top:60px">1<span class="step step--minus"></span><span class="step step--plus"></span></div>
  <div class="plan-cell" style="top:130px">$297</div>
  <div class="plan-cell" style="top:201px">$497<span class="step step--minus"></span><span class="step step--plus"></span></div>
  <div class="plan-cell plan-cell--profit" style="top:271px">$19,200</div>
  <div class="plan-bar"></div>
</div>

<div class="plan plan--enterprise" style="left:900px">
  <div class="plan-head">ENTERPRISE</div>
  <div class="plan-cell" style="top:60px">1<span class="step step--minus"></span><span class="step step--plus"></span></div>
  <div class="plan-cell" style="top:130px">$2500</div>
  <div class="plan-cell" style="top:201px">$4000<span class="step step--minus"></span><span class="step step--plus"></span></div>
  <div class="plan-cell plan-cell--profit" style="top:271px">$144,000</div>
  <div class="plan-bar"></div>
</div>

<div class="total">Monthly profit by the end of year 8: <strong>$172,800</strong></div>
</body>
</html>
```